Brisk Cloths, wipes multipack branding 3 types in 1 family

Brisk Cloths is a wipe producing company. For some information see our (not completed) website at briskcloths-example.nl. We also have a product named Palmbreeze (see Palmbreeze-example.com).
Our philosophy is to produce environmental friendly wipes only. We are doing that by using both bamboo and 100% bioviscose as Nonwoven. Both are biodegradable and compostable. We produce single packed wipes and multipacks (think about hygiene for hand, deodorant wipes and playtime wipes (for cleaning sex toys)). We are looking for designs for our multipacks (6 to 10 pieces per package). The size of the unfolded package foil is about 150 x 190mm (width x height) (but varies depending on the material and the number of wipes).
The branding should be modern, fresh and in line with our thoughts.

We want to have 3 packages designed for:
- Clean2Palms multipack 6 pieces
- Deodorant wipes multipack 6 pieces
- Playtime wipes multipack 10 pieces
All should have the look and feel of our Brisk Cloths logo / branding, and belong to the same family of products (to be recognised they belong together).

I added our logo as well as some examples of other packages we have been creating as samples. At first we have been thinking about using that design for multipacks as well, but we were not that happy about that.
Please consider them as a style that we liked.

Target Market(s)

Consumers
- Festival people (Clean2Palms and Deodorant)
- Adults with children (Clean2Palms)
- Travelers (Clean2Palm and Deodorant)
- Business people (Deodorant)
- Erotic industry (Playtime wipes)

Font styles to use
Sans Serif

Colors

Designer to choose colors to be used in the design.

Requirements
Must have
• A family in branding, recognisability as being part of 1 family of products.
• Branded with our logo (as attached).
• Necessary and mandatory information on the back of the package.
Nice to have
• Designs that fit to the purpose of the wipes.
• Different Colors for the different products.
• Chosen font is just because it is modern. Could be any other modern font as well.
Should not have
• Old fashioned style.
• Too much focus on the "green-ness" of the products.

```html
<!DOCTYPE html>
<html lang="en">
<head>
<meta charset="utf-8">
<title>Brisk Cloths – Multipack Family</title>
<link rel="stylesheet" href="https://fonts.googleapis.com/css2?family=Poppins:wght@400;600;700;800&display=swap">
<style>
  :root {
    --page: #ffffff;
    --foil: #ffffff;
    --seal: #eceef0;
    --foil-edge: #e1e4e7;
    --ink: #3d4148;
    --brand: #4aa3bf;
    --mint: #a1d3c9;
    --mint-deep: #6fbcad;
    --sky: #9fd4e4;
    --sky-deep: #5fb6cf;
    --rose: #d9b6c9;
    --rose-deep: #cf94b3;
  }
  * { box-sizing: border-box; margin: 0; padding: 0; }
  html, body { width: 1200px; height: 1200px; overflow: hidden; background: var(--page); }
  body { position: relative; font-family: "Poppins", sans-serif; }

  .pack {
    position: absolute;
    width: 492px;
    height: 280px;
    filter: drop-shadow(0 6px 10px rgba(0,0,0,0.08));
  }
  .pack--hands { left: 108px; top: 148px; --tone: var(--mint); --tone-deep: var(--mint-deep); }
  .pack--fresh { left: 356px; top: 460px; --tone: var(--sky);  --tone-deep: var(--sky-deep); }
  .pack--care  { left: 600px; top: 772px; --tone: var(--rose); --tone-deep: var(--rose-deep); }

  .pack__foil { position: absolute; inset: 0; width: 492px; height: 280px; }
  .pack__band { fill: var(--tone); }
  .pack__icon { stroke: var(--tone-deep); fill: none; stroke-width: 1.6; stroke-linecap: round; stroke-linejoin: round; }

  .brand {
    position: absolute;
    left: 76px;
    top: 144px;
    transform: translate(-50%, -50%) rotate(-90deg);
    display: flex;
    align-items: center;
    gap: 10px;
    white-space: nowrap;
  }
  .brand__dot { width: 16px; height: 16px; border-radius: 50%; background: var(--brand); }
  .brand__name {
    font-weight: 600;
    font-size: 21px;
    line-height: 22px;
    letter-spacing: 0.5px;
    color: var(--ink);
    text-transform: uppercase;
  }

  .pack__title {
    position: absolute;
    left: 178px;
    top: 66px;
    font-weight: 800;
    font-size: 44px;
    line-height: 48px;
    letter-spacing: -0.5px;
    color: #ffffff;
    white-space: nowrap;
  }
  .pack__claims {
    position: absolute;
    left: 179px;
    top: 179px;
    font-size: 11.5px;
    line-height: 16.5px;
    color: var(--ink);
    white-space: nowrap;
  }
  .pack__count {
    position: absolute;
    left: 448px;
    top: 234px;
    transform: translate(-50%, -50%) rotate(-90deg);
    color: var(--tone-deep);
    white-space: nowrap;
    display: flex;
    flex-direction: column;
    align-items: center;
    line-height: 10px;
  }
  .pack__count b { font-weight: 800; font-size: 12px; }
  .pack__count span { font-size: 8px; }
</style>
</head>
<body>

<section class="pack pack--hands" aria-label="Clean2Palms multipack">
  <svg class="pack__foil" viewBox="0 0 492 280" aria-hidden="true">
    <rect x="1" y="4" width="490" height="272" rx="6" fill="var(--foil)" stroke="var(--foil-edge)"/>
    <rect x="1" y="4" width="14" height="272" rx="4" fill="var(--seal)"/>
    <rect x="477" y="4" width="14" height="272" rx="4" fill="var(--seal)"/>
    <path class="pack__band" d="M152 8 L406 8 L424 26.9 L406 45.7 L424 64.6 L406 83.4 L424 102.3 L406 121.1 L424 140 L406 158.9 L424 177.7 L406 196.6 L424 215.4 L406 234.3 L424 253.1 L406 272 L152 272 Q144 228 152 184 Q160 140 152 96 Q144 52 152 8 Z"/>
    <g class="pack__icon">
      <circle cx="449" cy="116" r="11"/><line x1="441" y1="108" x2="457" y2="124"/>
      <circle cx="444" cy="118" r="1.6"/><circle cx="453" cy="112" r="1.6"/>
      <path d="M449 168 L459 185 L439 185 Z"/>
    </g>
  </svg>
  <div class="brand"><span class="brand__dot"></span><span class="brand__name">Brisk<br>Cloths</span></div>
  <h2 class="pack__title">clean<br>2 palms</h2>
  <p class="pack__claims">With antibacterial effectiveness<br>Biodegradable</p>
  <p class="pack__count"><b>6</b><span>pcs</span></p>
</section>

<section class="pack pack--fresh" aria-label="Fresh go multipack">
  <svg class="pack__foil" viewBox="0 0 492 280" aria-hidden="true">
    <rect x="1" y="4" width="490" height="272" rx="6" fill="var(--foil)" stroke="var(--foil-edge)"/>
    <rect x="1" y="4" width="14" height="272" rx="4" fill="var(--seal)"/>
    <rect x="477" y="4" width="14" height="272" rx="4" fill="var(--seal)"/>
    <path class="pack__band" d="M152 8 L406 8 L424 26.9 L406 45.7 L424 64.6 L406 83.4 L424 102.3 L406 121.1 L424 140 L406 158.9 L424 177.7 L406 196.6 L424 215.4 L406 234.3 L424 253.1 L406 272 L152 272 Q144 228 152 184 Q160 140 152 96 Q144 52 152 8 Z"/>
    <g class="pack__icon">
      <circle cx="449" cy="116" r="11"/><line x1="441" y1="108" x2="457" y2="124"/>
      <circle cx="444" cy="118" r="1.6"/><circle cx="453" cy="112" r="1.6"/>
      <path d="M449 168 L459 185 L439 185 Z"/>
    </g>
  </svg>
  <div class="brand"><span class="brand__dot"></span><span class="brand__name">Brisk<br>Cloths</span></div>
  <h2 class="pack__title">fresh<br>go</h2>
  <p class="pack__claims">With antibacterial effectiveness<br>Biodegradable</p>
  <p class="pack__count"><b>6</b><span>pcs</span></p>
</section>

<section class="pack pack--care" aria-label="Intimate care multipack">
  <svg class="pack__foil" viewBox="0 0 492 280" aria-hidden="true">
    <rect x="1" y="4" width="490" height="272" rx="6" fill="var(--foil)" stroke="var(--foil-edge)"/>
    <rect x="1" y="4" width="14" height="272" rx="4" fill="var(--seal)"/>
    <rect x="477" y="4" width="14" height="272" rx="4" fill="var(--seal)"/>
    <path class="pack__band" d="M152 8 L406 8 L424 26.9 L406 45.7 L424 64.6 L406 83.4 L424 102.3 L406 121.1 L424 140 L406 158.9 L424 177.7 L406 196.6 L424 215.4 L406 234.3 L424 253.1 L406 272 L152 272 Q144 228 152 184 Q160 140 152 96 Q144 52 152 8 Z"/>
    <g class="pack__icon">
      <circle cx="449" cy="116" r="11"/><line x1="441" y1="108" x2="457" y2="124"/>
      <circle cx="444" cy="118" r="1.6"/><circle cx="453" cy="112" r="1.6"/>
      <path d="M449 168 L459 185 L439 185 Z"/>
    </g>
  </svg>
  <div class="brand"><span class="brand__dot"></span><span class="brand__name">Brisk<br>Cloths</span></div>
  <h2 class="pack__title">intimate<br>care</h2>
  <p class="pack__claims">With antibacterial effectiveness<br>Biodegradable</p>
  <p class="pack__count"><b>10</b><span>pcs</span></p>
</section>

</body>
</html>
```